Carpet cleaning company focused on high quality needs business cards

We are a growing company that just merged with another company and need to design a new business card. We do both residential as well as commercial cleaning. We do carpet, tile & grout, upholstery, hard floors, and stain & pet odor removal. We treat our customers like family and strive to achieve outstanding results with every job.

```html
<!DOCTYPE html>
<html lang="en">
<head>
<meta charset="utf-8">
<title>Brightloom Steam Cleaning – Business Card</title>
<link rel="stylesheet" href="https://fonts.googleapis.com/css2?family=Poppins:wght@400;500;700;800&display=swap">
<style>
  :root{
    --stage:#2a2a2c;
    --card:#ffffff;
    --red:#ee4540;
    --red-deep:#d9352f;
    --red-line:#f19a95;
    --ink:#1b1b1b;
    --ink-soft:#333333;
    --link:#1f3a5a;
    --white:#ffffff;
  }
  *{box-sizing:border-box;margin:0;padding:0}
  html,body{width:1200px;height:1108px;overflow:hidden}
  body{background:var(--stage);font-family:"Poppins",sans-serif;position:relative}

  .card{position:absolute;top:186px;width:420px;height:735px;border-radius:26px;overflow:hidden}
  .card-front{left:150px;background:var(--card);padding:40px 24px 0;text-align:center;color:var(--ink)}
  .card-back{left:630px;background:var(--red)}

  .brand-row{display:flex;align-items:flex-end;gap:14px;height:200px;padding-left:16px}
  .mascot-art{width:176px;height:200px;border-radius:6px;flex:none;
    background:linear-gradient(180deg,#e8eef4 0%,#d6e3ee 55%,var(--red) 55%,var(--red-deep) 100%)}
  .wordmark{text-align:left;font-weight:800;color:var(--ink);line-height:1;padding-bottom:6px}
  .wordmark-name{display:block;font-size:32px;letter-spacing:-0.5px}
  .wordmark-sub{display:block;font-size:18px;margin-top:6px;line-height:1.05}

  .tagline{margin-top:18px;font-size:16px;font-weight:500;letter-spacing:0.4px;color:var(--ink);white-space:nowrap}
  .person-name{margin-top:16px;font-size:26px;font-weight:500;color:var(--red);letter-spacing:0.3px;line-height:1.5}
  .person-title{font-size:20px;color:var(--ink-soft);line-height:1.5}

  .divider{display:flex;align-items:center;gap:12px;margin:10px 16px}
  .divider::before,.divider::after{content:"";flex:1;height:1.5px;background:var(--red-line)}
  .icon-set{display:flex;gap:7px}
  .icon{width:34px;height:34px;border-radius:5px;background:var(--red);display:flex;align-items:center;justify-content:center}

  .contact{font-size:20px;line-height:1.5;color:var(--ink-soft)}
  .contact .web{color:var(--link)}
  .rule{height:1.5px;background:var(--red-line);margin:10px 46px}
  .address{font-size:20px;line-height:1.45;color:var(--ink-soft)}

  .services{margin-top:14px;font-size:16.5px;font-weight:500;line-height:1.5;color:var(--ink)}
  .services .line{display:block;white-space:nowrap}
  .services .dot{display:inline-block;width:8px;height:8px;border-radius:50%;background:var(--red);margin:0 5px 2px}

  .back-pattern{position:absolute;inset:0;
    background:linear-gradient(135deg,#f05a44 0%,var(--red) 45%,#e23a34 100%)}
  .back-mark{position:absolute;left:0;right:0;top:440px;text-align:center;color:var(--white);font-weight:800;line-height:1}
  .back-mark .wordmark-name{font-size:36px}
  .back-mark .wordmark-sub{font-size:19px;margin-top:6px}
</style>
</head>
<body>
  <section class="card card-front">
    <div class="brand-row">
      <div class="mascot-art" role="img" aria-label="Illustration of a smiling cleaning technician holding a steam wand over a red floor panel"></div>
      <div class="wordmark">
        <span class="wordmark-name">Brightloom</span>
        <span class="wordmark-sub">STEAM<br>CLEANING</span>
      </div>
    </div>
    <p class="tagline">RESIDENTIAL &amp; COMMERCIAL CLEANING</p>
    <h1 class="person-name">DANIEL REYES</h1>
    <p class="person-title">Managing Director</p>
    <div class="divider">
      <div class="icon-set">
        <span class="icon"><svg width="20" height="20" viewBox="0 0 24 24" fill="none" stroke="#fff" stroke-width="2"><path d="M5 4h4l2 5-2.5 1.5a11 11 0 0 0 5 5L15 13l5 2v4a2 2 0 0 1-2 2A16 16 0 0 1 3 6a2 2 0 0 1 2-2z"/></svg></span>
        <span class="icon"><svg width="20" height="20" viewBox="0 0 24 24" fill="none" stroke="#fff" stroke-width="2"><rect x="3" y="5" width="18" height="14" rx="1"/><path d="M3 6l9 7 9-7"/></svg></span>
        <span class="icon"><svg width="20" height="20" viewBox="0 0 24 24" fill="none" stroke="#fff" stroke-width="2"><circle cx="12" cy="12" r="9"/><path d="M3 12h18M12 3a14 14 0 0 1 0 18M12 3a14 14 0 0 0 0 18"/></svg></span>
      </div>
    </div>
    <p class="contact">044-555 0142 78<br>hello@brightloom.com<br><span class="web">www.brightloomclean.com</span></p>
    <div class="rule"></div>
    <p class="address">87, Marlowe Lane<br>Eastvale, 40218</p>
    <div class="rule"></div>
    <p class="services">
      <span class="line">Carpet<span class="dot"></span>Tile &amp; Grout<span class="dot"></span>Upholstery</span>
      <span class="line">Hard floors &amp; Stain<span class="dot"></span>Pet Odor Removal</span>
    </p>
  </section>

  <section class="card card-back">
    <div class="back-pattern" role="img" aria-label="Repeating tonal red pattern of the company name"></div>
    <div class="back-mark">
      <span class="wordmark-name">Brightloom</span>
      <span class="wordmark-sub">STEAM CLEANING</span>
    </div>
  </section>
</body>
</html>
```